Guaranteed Job - Sleek Sexy Business Card UV Spot

Im looking for a sleek and sexy business card, that resembles elite or VIP status status.
our business is corinvale.example
you can view our products on there, but our main audience for handing out our cards will be for people in the hospitality industry, so it will need to impress high management and CEO of hotels and restaurants, bars, clubs etc...
the card features will have UV spot on both sides, 400gsm stock. standard size.
Artwork should be 86 x 54mm + 2mm bleed = 90 x 58mm
it should have a nice "unique" uv spot pattern that highlights the card, not a repeated pattern, theres no originality there, and it will be disregarded.
The written material will be:
Corin Vale Hospitality College (logo)
Tobin Marsh
Director
Phone: 1300 615 737
Mobile: 0455 817 296
Email: info@corinvale.example
website: www.corinvale.example
I'm looking for originality here, i don't want just a simple stock card, want something that has a wow factor for people.
You will find the logo attached. you may invert the white to black words to suit the background as you please.
thank you and good luck
As a side note, ive received a lot of proposals, im too busy to give feedback to each and every one, so if i havent provided feedback for your design within 24 hours, then consider it not acceptable, and you could resubmit another design.
So far i have not seen any design that stood out for me, they all seem pretty generic. there nothing thats unique, i would figure for the amount that im offering, that people would put some more effort and creativity into the design.
so far over 200 designs submitted, and nothing i have seen looks very original, everything looks like a different variation of the same stuff, i said it very clearly i wanted something unique, the only thing that has come close to it so far is this one
Reason: Ive received alot of design concepts and i have reviewed everyone, but i havent had time to give feedback to every single one, only the ones that have interested me, if i havent responded, its because i havent found it good enough.
so far only a few design have been on par with what ive been looking for, an attractive eye popping design.
heres a few of them,
http://files.pixelbazaar.example/design_img/51736/62418/62418_2840915_51736_image.jpg
http://files.pixelbazaar.example/design_img/51736/68254/68254_2841377_51736_image.jpg
theyre, both unique and original, and eye catching, the only thing theyre missing is the sexyness.
if you still think you have some creativity left in your minds, then throw it on here.
Reason: Sorry guys for the delay, I was in a serious accident and out of commission for the past few months, I'm just slowly recovering now, please bare with me as i try to attend to this project, it may take me awhile as I have other projects that are on standby, I'm not 100% at the moment, so im extending the deadline for 2 weeks right now. Thanks for your patience.
Hospitality

```html
<!DOCTYPE html>
<html lang="en">
<head>
<meta charset="utf-8">
<title>Corin Vale Hospitality College – Business Card</title>
<link rel="stylesheet" href="https://fonts.googleapis.com/css2?family=Roboto+Condensed:wght@400;700&display=swap">
<style>
  :root {
    --page-bg: #ffffff;
    --card-bg: #1e2630;
    --card-glow: #3d4857;
    --ink-white: #ffffff;
    --ink-blue: #4ba3dc;
    --mark-line: #3a4554;
  }
  * { margin: 0; padding: 0; box-sizing: border-box; }
  html, body {
    width: 1200px;
    height: 1000px;
    overflow: hidden;
    background: var(--page-bg);
  }
  .canvas {
    position: relative;
    width: 1200px;
    height: 1000px;
    font-family: "Roboto Condensed", "Arial Narrow", sans-serif;
  }
  .card {
    position: absolute;
    left: 308px;
    width: 585px;
    height: 335px;
    background: var(--card-bg);
    overflow: hidden;
  }
  .card--front {
    top: 151px;
    border-bottom-right-radius: 50px;
  }
  .card--back {
    top: 535px;
    border-bottom-left-radius: 50px;
  }

  /* Front */
  .brand {
    position: absolute;
    left: 80px;
    top: 98px;
    color: var(--ink-white);
    font-weight: 700;
    text-transform: uppercase;
    line-height: 1;
  }
  .brand__name {
    display: block;
    font-size: 44px;
    letter-spacing: 0.5px;
  }
  .brand__tagline {
    display: block;
    margin-top: 6px;
    font-size: 17px;
    letter-spacing: 0.6px;
  }
  .brand-accent {
    position: absolute;
    left: 300px;
    top: 40px;
    width: 300px;
    height: 300px;
    border-radius: 50%;
    background: radial-gradient(circle at 40% 40%, var(--card-glow) 0%, #2a3340 45%, var(--card-bg) 80%);
  }

  /* Back */
  .back-mark {
    position: absolute;
    left: 190px;
    top: 62px;
    width: 128px;
    height: 128px;
    border: 1px solid var(--mark-line);
    border-radius: 50%;
  }
  .contact {
    position: absolute;
    left: 360px;
    top: 78px;
    color: var(--ink-blue);
  }
  .contact__name {
    color: var(--ink-white);
    font-size: 32px;
    font-weight: 700;
    line-height: 1;
    letter-spacing: 0.3px;
    margin-bottom: 6px;
  }
  .contact__line {
    font-size: 12px;
    line-height: 16px;
    white-space: nowrap;
  }
  .contact__line--spaced {
    letter-spacing: 3.6px;
  }
  .contact__role {
    letter-spacing: 10.4px;
  }
</style>
</head>
<body>
<main class="canvas">
  <section class="card card--front" aria-label="Card front">
    <div class="brand-accent" aria-hidden="true"></div>
    <h1 class="brand">
      <span class="brand__name">Corin Vale</span>
      <span class="brand__tagline">Hospitality College</span>
    </h1>
  </section>

  <section class="card card--back" aria-label="Card back">
    <div class="back-mark" aria-hidden="true"></div>
    <div class="contact">
      <p class="contact__name">Tobin Marsh</p>
      <p class="contact__line contact__role">Director</p>
      <p class="contact__line contact__line--spaced">P: 1300 615 737</p>
      <p class="contact__line contact__line--spaced">M: 0455 817 296</p>
      <p class="contact__line">E: info@corinvale.example</p>
      <p class="contact__line">W: www.corinvale.example</p>
    </div>
  </section>
</main>
</body>
</html>
```